Investment website design - investing in mutual funds

I need a design of a website (only homepage for now) dedicated to investment in mutual funds. Attached is a mock up with all the elements the homepage design should contain. The homepage should contain a logo in the upper left corner, the domain the website will run on is www.perovalstrinka.cz , in the upper right corner there should be 2 buttons or links SIGN UP / SIGN IN. The bottom of the homepage should contain links to ABOUT US, FAQ, PRIVACY POLICY, CONTACT US.
Now the main elements on the homepage
1) Video that will explain how the investment works exactly, under this video we will have 3 illustrated icons like the ones attached (see 2nd attachement) that will show the potential investor what exactly they could get when investing with us (education for kids, happy life after they retire, regular monthly payment for the rest of their life).
2) On the right side next to the video we will have a calculator where a potential investor can play with the numbers, the investor can fill in the MONTHLY PAYMENT that he wants to invest regularly every month, the time frame of the investment - for how long he wants to invest. Once the potential investor selects those 2 variables we will calculate for him 2 options - either he can get a ONE TIME PAYOUT once he reaches his investment horizon or he can get a regular monthly payment for the rest of his life. Under the laculator there will be a button 'I want to invest ->'. The functionality of the calculator should be similar to the calculator that can be found here http://www.brodavbank.cz/brodav-podilove-fondy/ and https://felbo.cz/.
The design should look similar to https://felbo.cz/ (font, colors, logo). We prefer white background in the area where we have the video and calculator. We also like the design of www.tarvupo.com. Let me know if you have any questions.

```html
<!DOCTYPE html>
<html lang="en">
<head>
<meta charset="utf-8">
<title>perovalstrinka.cz – Mutual Fund Investing</title>
<link href="https://fonts.googleapis.com/css2?family=Roboto:wght@300;400;500&display=swap" rel="stylesheet">
<style>
  :root {
    --hero-top: #c97b6f;
    --hero-mid: #e5806a;
    --hero-deep: #b8533b;
    --accent: #a83a22;
    --accent-text: #e04a2c;
    --white: #ffffff;
    --field-bg: rgba(255,255,255,0.16);
    --field-line: rgba(255,255,255,0.35);
    --teal: #2e8d96;
    --body-grey: #5a5a5a;
    --footer-grey: #6b6b6b;
    --player-dark: #1e1e1e;
    --player-mid: #2e2e2e;
    --video-bg: #f6ddd6;
  }
  * { box-sizing: border-box; margin: 0; padding: 0; }
  html, body { width: 1200px; height: 1073px; overflow: hidden; background: var(--white); }
  body { font-family: "Roboto", Arial, sans-serif; position: relative; }

  .hero {
    position: absolute; left: 0; top: 0; width: 1200px; height: 668px;
    background:
      radial-gradient(ellipse 260px 200px at 890px 440px, rgba(226,110,100,0.55), transparent 70%),
      linear-gradient(90deg, rgba(150,70,55,0.25) 0%, transparent 30%, transparent 60%, rgba(150,50,30,0.35) 100%),
      linear-gradient(180deg, var(--hero-top) 0%, var(--hero-mid) 35%, #d46a4f 70%, var(--hero-deep) 100%);
  }

  .brand { position: absolute; left: 57px; top: 63px; display: flex; align-items: center; gap: 10px; }
  .brand-dot { width: 60px; height: 60px; border-radius: 50%; background: var(--white); }
  .brand-name { color: var(--white); font-size: 36px; font-weight: 400; letter-spacing: 0.5px; }

  .account-nav { position: absolute; top: 77px; right: 72px; display: flex; align-items: center; gap: 17px; }
  .account-nav a { color: var(--white); text-decoration: none; font-size: 16px; }
  .account-nav .sign-in { background: var(--accent); padding: 8px 8px; height: 33px; display: block; }

  .video-player { position: absolute; left: 48px; top: 242px; width: 566px; height: 319px; box-shadow: 0 2px 8px rgba(0,0,0,0.45); }
  .video-frame { width: 566px; height: 271px; background: linear-gradient(180deg, #f8e3dd, var(--video-bg)); }
  .controls { height: 48px; width: 566px; background: linear-gradient(180deg, var(--player-mid), var(--player-dark)); position: relative; color: #999; font-size: 9px; }
  .controls .sep { position: absolute; top: 0; width: 1px; height: 48px; background: #444; }
  .pause { position: absolute; left: 22px; top: 17px; width: 10px; height: 13px; border-left: 3px solid #ccc; border-right: 3px solid #ccc; }
  .track { position: absolute; left: 74px; top: 19px; width: 212px; height: 9px; border-radius: 5px; background: #0c0c0c; }
  .track-fill { width: 124px; height: 9px; border-radius: 5px; background: linear-gradient(180deg,#7b8790,#4c5760); }
  .knob { position: absolute; width: 17px; height: 17px; border-radius: 50%; background: radial-gradient(circle at 40% 35%, #fff, #aaa); top: -4px; }
  .tooltip { position: absolute; left: 101px; top: -33px; width: 47px; height: 19px; background: #111; color: #ddd; font-size: 9px; text-align: center; line-height: 19px; border-radius: 2px; }
  .tooltip::after { content: ""; position: absolute; left: 19px; top: 19px; border: 5px solid transparent; border-top-color: #111; }
  .time { position: absolute; left: 296px; top: 19px; line-height: 10px; }
  .volume-icon { position: absolute; left: 379px; top: 19px; }
  .vol-track { position: absolute; left: 395px; top: 20px; width: 66px; height: 7px; border-radius: 4px; background: #0c0c0c; }
  .vol-fill { width: 30px; height: 7px; border-radius: 4px; background: #5e6b74; }
  .hd { position: absolute; left: 482px; top: 18px; width: 20px; text-align: center; font-weight: 500; font-size: 10px; }
  .fullscreen { position: absolute; left: 531px; top: 17px; }

  .calculator { position: absolute; left: 669px; top: 185px; width: 460px; color: var(--white); }
  .calculator h1 { font-weight: 400; font-size: 38px; text-align: center; text-shadow: 0 1px 2px rgba(0,0,0,0.2); height: 48px; }
  .field { position: absolute; left: 0; width: 460px; height: 52px; background: var(--field-bg); border: 1px solid var(--field-line); font-size: 18px; padding: 0 18px; line-height: 50px; font-weight: 300; }
  .field.monthly-in { top: 60px; }
  .field.one-time { top: 221px; }
  .field.monthly-out { top: 311px; padding-left: 21px; }
  .length-label { position: absolute; left: 1px; top: 126px; font-size: 18px; font-weight: 300; }
  .range { position: absolute; left: 0; top: 177px; width: 460px; height: 1px; background: rgba(255,255,255,0.7); }
  .range-thumb { position: absolute; left: 53px; top: -16px; width: 32px; height: 32px; border-radius: 50%; background: rgba(255,255,255,0.35); }
  .range-thumb::after { content: ""; position: absolute; left: 5px; top: 5px; width: 22px; height: 22px; border-radius: 50%; background: var(--white); }
  .range-min, .range-max { position: absolute; top: 182px; font-size: 14px; }
  .range-min { left: 0; }
  .range-max { right: 0; }
  .or { position: absolute; left: 0; width: 466px; top: 283px; text-align: center; font-size: 18px; font-weight: 300; color: rgba(255,255,255,0.8); }
  .invest-btn { position: absolute; right: 0; top: 382px; width: 189px; height: 52px; background: var(--accent); border: 1px solid rgba(255,255,255,0.25); color: var(--white); font-size: 18px; display: flex; align-items: center; justify-content: center; gap: 14px; text-decoration: none; }

  .benefit { position: absolute; top: 700px; width: 292px; }
  .benefit-art { position: absolute; width: 120px; height: 120px; background: linear-gradient(160deg, #f0a36a, #2e8d96); border-radius: 8px; opacity: 0.85; }
  .benefit h2 { position: absolute; top: 150px; font-size: 17px; font-weight: 400; color: var(--teal); white-space: nowrap; }
  .benefit p { position: absolute; top: 184px; width: 292px; font-size: 8.3px; line-height: 10px; color: var(--body-grey); }
  .benefit p span { color: var(--accent-text); }
  .benefit.education { left: 115px; }
  .benefit.education .benefit-art { left: 25px; top: 25px; width: 115px; height: 90px; }
  .benefit.education h2 { left: 8px; }
  .benefit.income { left: 455px; text-align: center; }
  .benefit.income .benefit-art { left: 95px; top: 12px; width: 130px; height: 126px; }
  .benefit.income h2 { left: 0; width: 292px; top: 148px; }
  .benefit.income p { top: 178px; }
  .benefit.retirement { left: 795px; text-align: right; }
  .benefit.retirement .benefit-art { left: 178px; top: 4px; width: 122px; height: 136px; }
  .benefit.retirement h2 { right: 5px; }
  .benefit.retirement p { top: 178px; }

  .site-footer { position: absolute; top: 1013px; left: 0; width: 1200px; text-align: center; font-size: 19px; color: var(--footer-grey); }
  .site-footer a { color: var(--footer-grey); text-decoration: none; }
  .site-footer .divider { margin: 0 12px; }
</style>
</head>
<body>
  <header class="hero" role="img" aria-label="Blurred city skyline at sunset with a pink piggy bank, tinted coral">
  </header>

  <div class="brand">
    <span class="brand-dot"></span>
    <span class="brand-name">perovalstrinka.cz</span>
  </div>

  <nav class="account-nav">
    <a href="#">SIGN UP</a>
    <a href="#" class="sign-in">SIGN IN</a>
  </nav>

  <section class="video-player">
    <div class="video-frame" role="img" aria-label="Video still: rising orange arrow over three golden bars"></div>
    <div class="controls">
      <span class="pause"></span>
      <span class="sep" style="left:54px"></span>
      <div class="track">
        <div class="track-fill"></div>
        <span class="knob" style="left:116px"></span>
        <span class="tooltip">01:46</span>
      </div>
      <span class="time">01:46 / 03:09</span>
      <span class="sep" style="left:366px"></span>
      <svg class="volume-icon" width="10" height="10" viewBox="0 0 10 10"><path d="M0 3h3l4-3v10L3 7H0z" fill="#aaa"/></svg>
      <div class="vol-track"><div class="vol-fill"></div><span class="knob" style="left:22px;top:-5px"></span></div>
      <span class="sep" style="left:471px"></span>
      <span class="hd">HD</span>
      <span class="sep" style="left:509px"></span>
      <svg class="fullscreen" width="13" height="13" viewBox="0 0 13 13" fill="none" stroke="#ccc" stroke-width="1.5"><path d="M1 4V1h3M9 1h3v3M12 9v3H9M4 12H1V9"/></svg>
    </div>
  </section>

  <section class="calculator">
    <h1>Our Online Calculator</h1>
    <div class="field monthly-in">Regular monthly Investment</div>
    <div class="length-label">Length Of Investments</div>
    <div class="range"><span class="range-thumb"></span></div>
    <span class="range-min">0</span>
    <span class="range-max">30&nbsp; years</span>
    <div class="field one-time">One time payout</div>
    <div class="or">OR</div>
    <div class="field monthly-out">Monthly payout</div>
    <a href="#" class="invest-btn">I want to Invest
      <svg width="10" height="14" viewBox="0 0 10 14"><path d="M2 1l6 6-6 6" stroke="#fff" stroke-width="2.4" fill="none"/></svg>
    </a>
  </section>

  <section class="benefit education">
    <div class="benefit-art" role="img" aria-label="Illustration of stacked books with a graduation cap"></div>
    <h2>Education for kids</h2>
    <p>Plan early for school fees and university costs. A steady monthly deposit grows over the years, so your children can <span>study</span> where they wish without loans weighing on the family budget later. Start with a small sum today.</p>
  </section>

  <section class="benefit income">
    <div class="benefit-art" role="img" aria-label="Illustration of a cuckoo clock dropping gold coins"></div>
    <h2>Passive Income</h2>
    <p>Receive a regular payment every month for the rest of your life. Your savings keep working in mutual funds while you enjoy a <span>stable income</span> that covers bills, travel and the small pleasures of everyday living.</p>
  </section>

  <section class="benefit retirement">
    <div class="benefit-art" role="img" aria-label="Illustration of a retiree swinging a golf club"></div>
    <h2>Happy Retirement</h2>
    <p>Retire on your own terms. Build a fund now and take it as one <span>payout</span> or as a monthly sum, then spend your free time on golf, family, travel and everything you postponed while working.</p>
  </section>

  <footer class="site-footer">
    <a href="#">About us</a><span class="divider">|</span><a href="#">FAQ</a><span class="divider">|</span><a href="#">Privacy Policy</a><span class="divider">|</span><a href="#">Contact</a>
  </footer>
</body>
</html>
```